Frischer, moderner, emotionaler Baumarkt-Onlineshop sucht passende Außendarstellung
Zielgruppe
Wir sind gerade im Aufbau eines Onlinebaumarktes. In diesem Baumarkt bekommt man vom Nagel bis hin zum neuen Fußboden alles was das Herz begehrt. Wir möchten der Begleiter für jeden Heimwerker sein, der eine gute Beratung, hochwertige Produkte und einen aufgeräumten Fachhandel sucht. Wir wollen einen emotionalen Onlineshop schaffen, bei dem das richtige Produkt dich sucht und nicht du stundenlang das richtige Produkt.
Aufgabenstellung
Wir möchten ein modernes und frisches Bild, der etwas eingestaubten Baumarktlandschaft vermitteln. Bei uns soll es Spaß machen, nach tollen Produkten zu stöbern. Der Kunde soll visuell angesprochen werden und sich intuitiv auf unseren Seiten bewegen können. Wenn man sich die gängigen Shopseiten anschaut, hat man eine ewig lange Navigation um zu seinem Produkt zu kommen. Wir möchten diesen Prozess, durch intelligente Filter gerne verkürzen, so dass jeder Laie sein Produkt ganz leicht findet.
Die Farben der Seite sollten sich an das Logo anlehnen oder diese auch einfließen lassen, damit die Seite wie aus einem Guss wirkt. Interessieren würde uns auch wie die Seite nicht nur auf dem Desktop aussieht, sondern auch seine Übersichtigkeit auf einem Tablet oder Smartphone beibehält.

```html
<!DOCTYPE html>
<html lang="de">
<head>
<meta charset="utf-8">
<title>heimwerkraum.de – Badmöbel</title>
<link href="https://fonts.googleapis.com/css2?family=Roboto+Condensed:wght@400;700&family=Arimo:wght@400;700&display=swap" rel="stylesheet">
<style>
:root{
  --navy:#1a3a8c;
  --green:#8cbd1f;
  --green-dark:#5f9e10;
  --orange:#f07d0a;
  --ink:#222;
  --panel:#e5e5e5;
  --footer:#e4e8f2;
  --link-blue:#3b5cc4;
}
*{box-sizing:border-box;margin:0;padding:0}
html,body{width:1200px;height:962px;overflow:hidden;background:#fff}
body{position:relative;font-family:"Arimo",sans-serif;color:var(--ink)}
.abs{position:absolute}

/* header */
.header{left:0;top:0;width:1200px;height:100px;border-bottom:2px solid #e6e6e6}
.brand{left:167px;top:30px;display:flex;align-items:center;gap:8px}
.brand-mark{width:18px;height:18px;background:var(--navy)}
.brand-name{font-family:"Roboto Condensed",sans-serif;font-weight:700;font-size:30px;color:var(--navy);letter-spacing:-.5px}
.search{left:396px;top:48px;width:232px;height:23px;border:2px solid #d8d8d8;font-size:10px;color:#888;padding:3px 6px}
.search svg{position:absolute;right:6px;top:3px}
.topnav{left:714px;top:0;width:324px;height:22px;border:1px solid #ddd;border-top:none;display:flex;font-size:10px;font-weight:700;color:#555}
.topnav span{padding:4px 9px;border-right:1px solid #ddd;white-space:nowrap}
.topnav span:last-child{border:none}
.cart{left:848px;top:44px;font-size:11px;font-weight:700;color:#555;letter-spacing:.5px}
.cart .sum{color:var(--orange);font-weight:400;margin-left:30px;font-size:9px}
.cart-sel{left:848px;top:63px;width:132px;height:17px;border:1px solid #e4e4e4;font-size:8px;color:#aaa;padding:3px 6px}
.cart-icon{left:988px;top:37px}

/* main */
.stage{left:166px;top:101px;width:872px;height:490px;background:var(--green)}
.side{left:167px;top:110px;width:162px}
.side-title{height:60px;background:var(--navy);color:#fff;font-size:29px;line-height:27px;padding:4px 15px}
.side-nav{background:var(--panel);margin-top:10px;padding:0 2px}
.side-nav li{list-style:none;height:31.5px;border-bottom:1px solid #fff;font-size:9.5px;font-weight:700;padding:10px 6px;display:flex;justify-content:space-between;background:#f3f3f3}
.side-nav li.active{background:#dde1f8;color:var(--navy)}
.seal{left:167px;top:411px;width:162px;height:60px;background:#fff;display:flex;gap:8px;padding:9px 3px;font-size:9.5px;color:#999;line-height:12px}
.seal i{width:40px;height:40px;border-radius:50%;background:#555;flex:none}
.seal b{color:#444}
.info{left:167px;top:481px;width:162px;height:110px;background:#fff}
.info h3{background:#eee;font-family:"Roboto Condensed",sans-serif;font-size:11px;color:#555;padding:9px 12px;height:31px}
.info p{font-size:8.5px;color:#aaa;padding:11px 7px 0;line-height:10.5px}

.product{left:351px;top:111px;width:513px;height:289px;background:#fff}
.vendor{left:25px;top:25px;font-size:10px;color:#7a9bd8}
.p-title{left:86px;top:15px;font-family:"Roboto Condensed",sans-serif;font-size:14px;line-height:15px}
.p-title b{font-size:15px}
.p-photo{left:97px;top:72px;width:71px;height:158px;background:linear-gradient(#fafafa,#dedede)}
.badge-no1{left:351px;top:0;width:162px;height:62px;background:var(--navy);color:#fff;font-size:23px;line-height:24px;padding:4px 24px}
.p-facts{left:216px;top:119px;font-family:"Roboto Condensed",sans-serif;font-size:9.5px;line-height:15.5px;width:116px;list-style:square}
.p-facts li{margin-left:8px}
.p-more{left:216px;top:212px;font-family:"Roboto Condensed",sans-serif;font-size:9.5px;text-decoration:underline}
.p-rate{left:216px;top:243px;font-family:"Roboto Condensed",sans-serif;font-size:9.5px}
.p-rate u{margin-left:10px}
.price{left:342px;top:124px;font-family:"Roboto Condensed",sans-serif;font-weight:700;font-size:31px;color:var(--orange)}
.vat{left:342px;top:168px;font-family:"Roboto Condensed",sans-serif;font-size:10px}
.buy{left:342px;top:186px;width:153px;height:41px;background:var(--orange);color:#fff;font-family:"Roboto Condensed",sans-serif;padding:2px 3px}
.buy b{font-size:12px;display:block}
.buy small{font-size:7.5px;font-weight:700}
.buy svg{position:absolute;right:8px;top:8px}
.ship{left:342px;top:233px;font-family:"Roboto Condensed",sans-serif;font-size:6.5px;color:var(--navy);text-decoration:underline;word-spacing:4px}

.details{left:351px;top:413px;width:513px;height:176px;background:#fff}
.tabs{left:9px;top:9px;display:flex;font-family:"Roboto Condensed",sans-serif;font-size:10px;font-weight:700}
.tabs span{padding:4px 10px;border:1px solid #ccc;background:#f4f4f4}
.tabs .on{background:var(--green-dark);color:#fff;border-color:var(--green-dark)}
.desc{left:13px;top:38px;font-size:6px;line-height:8px;width:300px}
.desc ul{margin-top:30px;margin-left:7px}
.share{left:368px;top:104px;font-family:"Roboto Condensed",sans-serif;font-weight:700;font-size:13px}
.share-icons{left:396px;top:125px;display:flex;gap:6px}
.share-icons i{width:22px;height:22px;border-radius:3px}

.related{left:875px;top:113px;width:155px;height:472px;background:#dcdcdc}
.rel-head{left:885px;top:102px;background:var(--green-dark);color:#fff;font-size:8px;font-weight:700;padding:4px 10px}
.card{left:885px;width:132px;background:#fff}
.card .ph{left:40px;width:50px;height:45px;background:linear-gradient(#cfcfcf,#8a8a8a);border-radius:6px}
.card .nm{left:12px;font-size:7.5px;font-weight:700;text-decoration:underline;white-space:nowrap}
.card .pr{left:12px;font-family:"Roboto Condensed",sans-serif;font-weight:700;font-size:18px;color:var(--orange)}
.card .pr sup{font-size:10px}
.card .add{right:5px;width:40px;height:31px;background:var(--orange)}
.card .add svg{position:absolute;left:6px;top:7px}

.chat{left:0;top:231px;width:57px;height:218px;background:var(--green)}
.chat .x{left:5px;top:4px;width:17px;height:17px;background:#fff;color:#000;font-size:14px;text-align:center;line-height:16px}
.chat .txt{left:10px;top:210px;transform:rotate(-90deg);transform-origin:left top;color:#fff;white-space:nowrap}
.chat .txt b{font-size:19px;display:block}
.chat .txt span{font-size:9.5px}

/* footer */
.footer{left:0;top:597px;width:1200px;height:122px;background:var(--footer)}
.fcol{top:0;height:122px;border-left:1px solid #c9cbd3;padding:12px 30px;font-size:8.5px;line-height:11px;color:#555}
.fcol h4{color:var(--link-blue);font-size:10px;margin-bottom:8px}
.fcol .tel{font-size:14px;font-weight:700;margin-top:10px;line-height:13px;color:#333}
.nl-field{margin-top:22px;width:180px;height:18px;border:1px solid #aab;background:#fff;font-size:7.5px;padding:3px;position:relative}
.nl-field i{position:absolute;right:0;top:0;width:18px;height:16px;background:var(--link-blue)}
</style>
</head>
<body>

<header class="abs header">
  <div class="abs brand"><span class="brand-mark"></span><span class="brand-name">heimwerkraum.de</span></div>
  <div class="abs search">Suche:
    <svg width="13" height="13" viewBox="0 0 13 13"><circle cx="5" cy="5" r="4" fill="none" stroke="#555" stroke-width="1.6"/><path d="M8 8l4 4" stroke="#555" stroke-width="1.8"/></svg>
  </div>
  <nav class="abs topnav"><span>Mein Konto</span><span>Merkzettel</span><span>Service/Hilfe ⌄</span><span>EUR <span style="color:#bbb;font-weight:400;padding:0">USD</span></span></nav>
  <div class="abs cart">WARENKORB<span class="sum">0,00</span></div>
  <div class="abs cart-sel">Positionen anzeigen</div>
  <svg class="abs cart-icon" width="42" height="45" viewBox="0 0 42 45"><path d="M4 5v28h34M8 33l-2 6M34 33l2 6" fill="none" stroke="#777" stroke-width="2"/><path d="M4 5l-2-3M16 2v12" stroke="#777" stroke-width="2"/><circle cx="8" cy="40" r="3" fill="#777"/><circle cx="34" cy="40" r="3" fill="#777"/></svg>
</header>

<div class="abs chat">
  <div class="abs x">✕</div>
  <div class="abs txt"><b>LIVE-Beratung</b><span>Wir beraten Sie kostenlos im Chat</span></div>
</div>

<main>
  <div class="abs stage"></div>

  <aside class="abs side">
    <div class="side-title">Bade-<br>zimmer</div>
    <ul class="side-nav">
      <li>Armaturen<span>⌄</span></li>
      <li>Badaccessoires<span>⌄</span></li>
      <li>Badewannen<span>⌄</span></li>
      <li>Badkeramik<span>⌄</span></li>
      <li class="active">Badmöbel<span>⌄</span></li>
      <li>Brause &amp; Duschzubehör<span>⌄</span></li>
      <li>Heizgeräte<span>⌄</span></li>
    </ul>
  </aside>
  <div class="abs seal"><i></i><div><b>Sicher</b> einkaufen<br>Kaufsiegel<br>zertifiziert</div></div>
  <div class="abs info"><h3>INFORMATIONEN</h3><p>Hilfe / Support<br><br>Über uns<br><br>Kontakt</p></div>

  <section class="abs product">
    <span class="abs vendor">Nordbad</span>
    <div class="abs p-title"><b>Badmöbel Set Lira</b><br>40 cm, bodenstehend<br>NB0451308822</div>
    <div class="abs p-photo" role="img" aria-label="Produktfoto: weißer Waschtischunterschrank mit Waschbecken"></div>
    <div class="abs badge-no1">Nr 1. in<br>Badmöbel</div>
    <ul class="abs p-facts">
      <li>Maße: H 844 x B 400 x T 330 mm</li>
      <li>Front: weiss hochglanz lackiert</li>
      <li>Korpus: weiss laminiert</li>
    </ul>
    <span class="abs p-more">weitere Details</span>
    <span class="abs p-rate">Bewertung: <u>Jetzt bewerten!</u></span>
    <div class="abs price">49,- €</div>
    <div class="abs vat">inkl. gesetzl. MwSt.</div>
    <div class="abs buy"><b>Online bestellen</b><small>Lieferzeit: ca. 3 - 5 Werktage</small>
      <svg width="36" height="24" viewBox="0 0 36 24"><path d="M2 6l4 6-4 6" fill="none" stroke="#fff" stroke-width="2.4"/><path d="M11 3h4l3 12h14l2-9H17" fill="none" stroke="#fff" stroke-width="2.4"/><circle cx="20" cy="20" r="2" fill="#fff"/><circle cx="30" cy="20" r="2" fill="#fff"/></svg>
    </div>
    <div class="abs ship">zzgl. Versandkosten: Versandkostenfrei</div>
  </section>

  <section class="abs details">
    <div class="abs tabs"><span class="on">Produktdetails</span><span>Bewertungen</span></div>
    <div class="abs desc">
      <b>Badmöbel Set Lira, 40 cm, bodenstehend</b><br><br><br>Besteht aus Waschtischunterschrank mit Waschtisch.
      <ul><li>Maße: H 844 x B 400 x T 330 mm</li><li>Front: weiss hochglanz lackiert</li><li>Korpus: weiss laminiert</li><li>1-Türig</li><li>verchromte Möbelgriffe</li><li>vormontiert</li></ul>
    </div>
    <div class="abs share">Weiterempfehlen</div>
    <div class="abs share-icons"><i style="background:#3f63b4"></i><i style="background:#3cb0e6"></i>
      <svg width="22" height="22" viewBox="0 0 22 22"><rect width="22" height="22" rx="3" fill="#9fd3ee"/><rect x="4" y="6" width="14" height="10" fill="#fff"/><path d="M4 6l7 6 7-6" fill="none" stroke="#6ab" stroke-width="1.2"/></svg>
    </div>
  </section>

  <aside class="abs related"></aside>
  <div class="abs rel-head">Kunden kauften auch</div>

  <div class="abs card" style="top:137px;height:122px">
    <div class="abs ph" style="top:8px" role="img" aria-label="Produktfoto: Ablaufgarnitur"></div>
    <div class="abs nm" style="top:64px;left:30px">Varlo Waschtis...</div>
    <div class="abs pr" style="top:82px;left:30px">2,<sup>96</sup> €</div>
    <div class="abs add" style="top:86px"><svg width="28" height="18" viewBox="0 0 36 24"><path d="M2 6l4 6-4 6" fill="none" stroke="#fff" stroke-width="2.4"/><path d="M11 3h4l3 12h14l2-9H17" fill="none" stroke="#fff" stroke-width="2.4"/><circle cx="20" cy="20" r="2" fill="#fff"/><circle cx="30" cy="20" r="2" fill="#fff"/></svg></div>
  </div>
  <div class="abs card" style="top:274px;height:143px">
    <div class="abs ph" style="top:7px" role="img" aria-label="Produktfoto: LED-Einbauleuchten"></div>
    <div class="abs nm" style="top:65px">Lumeta LED Ei...</div>
    <div class="abs pr" style="top:84px">81,<sup>99</sup> €</div>
    <div class="abs add" style="top:106px"><svg width="28" height="18" viewBox="0 0 36 24"><path d="M2 6l4 6-4 6" fill="none" stroke="#fff" stroke-width="2.4"/><path d="M11 3h4l3 12h14l2-9H17" fill="none" stroke="#fff" stroke-width="2.4"/><circle cx="20" cy="20" r="2" fill="#fff"/><circle cx="30" cy="20" r="2" fill="#fff"/></svg></div>
  </div>
  <div class="abs card" style="top:430px;height:143px">
    <div class="abs ph" style="top:8px" role="img" aria-label="Produktfoto: eckige LED-Einbauleuchten"></div>
    <div class="abs nm" style="top:66px">Lumeta LED Ei...</div>
    <div class="abs pr" style="top:84px">81,<sup>99</sup> €</div>
    <div class="abs add" style="top:106px"><svg width="28" height="18" viewBox="0 0 36 24"><path d="M2 6l4 6-4 6" fill="none" stroke="#fff" stroke-width="2.4"/><path d="M11 3h4l3 12h14l2-9H17" fill="none" stroke="#fff" stroke-width="2.4"/><circle cx="20" cy="20" r="2" fill="#fff"/><circle cx="30" cy="20" r="2" fill="#fff"/></svg></div>
  </div>
</main>

<footer class="abs footer">
  <div class="abs fcol" style="left:167px;width:200px">
    <h4>Service Hotline</h4>Telefonische Unterstützung und Beratung unter:
    <div class="tel">0180 - 555123</div><span style="font-size:7.5px">Mo-Fr, 09:00 - 17:00 Uhr</span>
  </div>
  <div class="abs fcol" style="left:367px;width:214px">
    <h4>Shop Service</h4>Defektes Produkt<br>Partnerprogramm<br>rechtliche Vorabinformationen<br>Kontakt<br>Versand und Zahlungsbedingungen<br>Rückgabe
  </div>
  <div class="abs fcol" style="left:581px;width:211px">
    <h4>Informationen</h4>Newsletter<br>Über uns<br>Datenschutz<br>Impressum
  </div>
  <div class="abs fcol" style="left:792px;width:246px;border-right:1px solid #c9cbd3">
    <h4>Newsletter</h4>Abonnieren Sie den kostenlosen Werkraum-Shop Newsletter und verpassen Sie keine Neuigkeit oder Aktion mehr aus dem Werkraum-Shop.
    <div class="nl-field">Ihre E-Mail Adresse<i></i></div>
  </div>
</footer>

</body>
</html>
```